Eine Willkommenseite (Startseite) für WohnFokus
Zielgruppe
Die Zielgruppe sind Kunden (Business, Privat und öffentliche Einrichtungen) die Immobilien über das Wohnfokus-Portal kostenlos suchen oder inserieren möchten. Quasi alle Besucher, die Immobilen über WohnFokus ohne Inseratkosten verkaufen, kaufen, vermieten, mieten und versteigern wollen.
Aufgabenstellung
Die Willkommenseite für WohnFokus.
Problemstellung: WohnFokus ist seit ca. 3 Monaten erfolgreich online. Die Immobilen Webseite von WohnFokus ist schlicht, dezent sowie funktionell aufgebaut. WohnFokus fehlt eine ansprechende Willkommenseite. Die Willkommenseite sollte emotional ansprechend und dem/der BesucherIn ein "Wow" entlocken sowie zu einem weiteren Surfen auf WohnFokus einladen.

```html
<!DOCTYPE html>
<html lang="de">
<head>
<meta charset="utf-8">
<title>WohnFokus – Willkommen</title>
<link rel="stylesheet" href="https://fonts.googleapis.com/css2?family=PT+Sans:wght@400;700&family=Open+Sans:wght@400;600&display=swap">
<style>
  :root {
    --blue: #4f7cc0;
    --blue-soft: #7b9acc;
    --button: #8aa8d8;
    --ink: #1b1b1b;
    --panel-top: #e6e6e6;
    --panel-low: #f1f1f1;
    --band: #e8e8e8;
    --line: #cfcfcf;
    --white: #ffffff;
    --muted: #555555;
  }
  * { box-sizing: border-box; margin: 0; padding: 0; }
  html, body { width: 1200px; height: 924px; overflow: hidden; background: var(--white); }
  body { position: relative; font-family: "Open Sans", Verdana, sans-serif; color: var(--ink); }

  .brand {
    position: absolute; left: 36px; top: 176px;
    font-family: "PT Sans", sans-serif; font-weight: 700; font-size: 52px;
    letter-spacing: -1px; color: var(--blue); line-height: 1;
  }

  .hero-panel {
    position: absolute; left: 466px; top: 131px; width: 697px; height: 402px;
    background: var(--panel-top);
  }
  .hero-panel .lower {
    position: absolute; left: 0; right: 0; top: 198px; bottom: 0;
    background: var(--panel-low); border-top: 3px solid var(--white);
  }
  .corner-notch {
    position: absolute; right: -36px; top: -52px; width: 100px; height: 100px;
    border-radius: 50%; background: var(--white);
  }
  .home-icon { position: absolute; right: 10px; top: 0; width: 34px; height: 32px; }

  .search {
    position: absolute; left: 103px; top: 61px; display: flex; gap: 8px;
  }
  .search-field {
    width: 348px; height: 33px; background: var(--white); border: 1px solid var(--line);
    display: flex; align-items: center; justify-content: space-between; padding: 0 10px;
    font-size: 18px; color: var(--muted);
  }
  .search-button {
    width: 102px; height: 33px; background: var(--button); color: var(--white);
    font-size: 19px; display: flex; align-items: center; justify-content: center;
  }

  .flags { position: absolute; right: 19px; top: 174px; display: flex; gap: 9px; }
  .flags svg { width: 22px; height: 14px; display: block; }

  .intro {
    position: absolute; left: 40px; top: 239px; width: 610px;
    font-size: 13.3px; line-height: 24px; color: var(--ink);
  }

  .globe {
    position: absolute; left: 407px; top: 290px; width: 66px; height: 66px; border-radius: 50%;
    background: radial-gradient(circle at 35% 35%, #9fc0ec, #3564ad 70%, #1f4584);
  }
  .tagline {
    position: absolute; left: 462px; top: 296px; width: 378px; height: 46px;
    background: var(--white); border-radius: 0 23px 23px 0;
    transform: rotate(-3deg); box-shadow: 0 2px 3px rgba(0,0,0,.25);
    font-family: "PT Sans", sans-serif; font-weight: 700; font-size: 23px;
    display: flex; align-items: center; padding-left: 38px; color: #333;
  }
  .tagline em { font-style: normal; color: var(--blue); margin: 0 6px; }

  .offers-title {
    position: absolute; left: 40px; top: 506px;
    font-family: "PT Sans", sans-serif; font-weight: 700; font-size: 22px; color: var(--blue);
  }
  .offers-band {
    position: absolute; left: 36px; top: 539px; width: 1127px; height: 238px; background: var(--band);
  }
  .offer-card {
    position: absolute; top: 17px; width: 260px; height: 202px; background: var(--white);
    border: 1px solid #d8d8d8;
  }
  .offer-photo { position: absolute; left: 12px; top: 12px; width: 235px; height: 157px; }
  .offer-caption {
    position: absolute; left: 12px; right: 12px; bottom: 8px; font-size: 11px; color: #333;
    display: flex; justify-content: space-between; align-items: center;
  }
  .doc-icon { width: 11px; height: 14px; }

  .more-bar {
    position: absolute; left: 36px; top: 777px; width: 1127px; height: 59px; background: var(--blue-soft);
  }
  .more-arrow { position: absolute; left: 673px; top: 17px; width: 34px; height: 26px; }
  .more-button {
    position: absolute; left: 723px; top: 12px; width: 386px; height: 37px;
    background: var(--white); border-radius: 18px; box-shadow: 0 2px 3px rgba(0,0,0,.25);
    font-family: "PT Sans", sans-serif; font-weight: 700; font-size: 22px; color: #333;
    display: flex; align-items: center; justify-content: center; gap: 6px;
  }
  .more-button u { color: var(--blue); }

  .footer {
    position: absolute; left: 36px; top: 852px; display: flex; align-items: center; gap: 16px;
    font-size: 13px; color: var(--ink);
  }
  .social { display: flex; gap: 8px; margin-left: 4px; }
  .social span { width: 26px; height: 26px; border-radius: 50%; display: block; }
</style>
</head>
<body>

  <div class="brand">WOHNFOKUS</div>

  <section class="hero-panel">
    <div class="corner-notch"></div>
    <svg class="home-icon" viewBox="0 0 34 32" aria-label="Startseite">
      <path d="M3 15 L16 4 L29 15" fill="none" stroke="#777" stroke-width="2.5"/>
      <rect x="7" y="14" width="18" height="14" fill="#eee" stroke="#777" stroke-width="2"/>
      <circle cx="24" cy="22" r="5" fill="#f0a030"/>
    </svg>

    <form class="search">
      <div class="search-field">
        <span>Schnellsuche...</span>
        <svg width="18" height="18" viewBox="0 0 18 18"><circle cx="7" cy="7" r="5" fill="none" stroke="#888" stroke-width="2"/><path d="M11 11 L16 16" stroke="#888" stroke-width="3"/></svg>
      </div>
      <div class="search-button">Suchen</div>
    </form>

    <div class="flags">
      <svg viewBox="0 0 22 14"><rect width="22" height="5" fill="#111"/><rect y="5" width="22" height="4" fill="#d00"/><rect y="9" width="22" height="5" fill="#fc0"/></svg>
      <svg viewBox="0 0 22 14"><rect width="22" height="14" fill="#d22"/><rect y="5" width="22" height="4" fill="#fff"/></svg>
      <svg viewBox="0 0 22 14"><rect width="22" height="14" fill="#e11"/><rect x="9.5" y="3" width="3" height="8" fill="#fff"/><rect x="7" y="5.5" width="8" height="3" fill="#fff"/></svg>
      <svg viewBox="0 0 22 14"><rect width="22" height="7" fill="#1c3d9c"/><rect y="7" width="22" height="7" fill="#d22"/></svg>
    </div>

    <div class="lower"></div>
    <p class="intro">Lorem ipsum dolor sit amet, consectetur adipisici elit, sed eiusmod tempor incidunt ut labore et dolore magna aliqua. Ut enim ad minim veniam, quis nostrud exercitation ullamco laboris nisi ut aliquid ex ea commodi consequat. Quis aute iure reprehenderit in voluptate velit esse cillum dolore eu fugiat nulla pariatur. Excepteur sint obcaecat cupiditat non proident, sunt in culpa qui officia deserunt.</p>
  </section>

  <div class="tagline">WIR SIND <em>WELTWEIT</em> TÄTIG!</div>
  <div class="globe" role="img" aria-label="Erdkugel mit kleinen Figuren darauf"></div>

  <h2 class="offers-title">AKTUELLE ANGEBOTE:</h2>
  <section class="offers-band">
    <article class="offer-card" style="left:17px">
      <div class="offer-photo" role="img" aria-label="Modernes Holzhaus vor Bergkulisse" style="background:linear-gradient(#6f9fd6 0%,#a9c6e6 45%,#b58450 70%,#6b6a5c 100%)"></div>
      <div class="offer-caption"><span>Österreich, Salzburg, Zell am See</span><svg class="doc-icon" viewBox="0 0 11 14"><path d="M1 1h6l3 3v9H1z" fill="#fff" stroke="#888"/></svg></div>
    </article>
    <article class="offer-card" style="left:294px">
      <div class="offer-photo" role="img" aria-label="Heller Wohnraum mit Parkett und Terrassentür" style="background:linear-gradient(90deg,#e4e2dc 0%,#d6d3cc 50%,#c9d8b8 80%,#b8a07a 100%)"></div>
      <div class="offer-caption"><span>Österreich, NÖ, Korneuburg</span><svg class="doc-icon" viewBox="0 0 11 14"><path d="M1 1h6l3 3v9H1z" fill="#fff" stroke="#888"/></svg></div>
    </article>
    <article class="offer-card" style="left:571px">
      <div class="offer-photo" role="img" aria-label="Weiße Villa mit Garten und Rasen" style="background:linear-gradient(#5f8a4a 0%,#e6e6e0 35%,#8fb15a 65%,#5e9a2e 100%)"></div>
      <div class="offer-caption"><span>Österreich, NÖ, Melk</span><svg class="doc-icon" viewBox="0 0 11 14"><path d="M1 1h6l3 3v9H1z" fill="#fff" stroke="#888"/></svg></div>
    </article>
    <article class="offer-card" style="left:848px">
      <div class="offer-photo" role="img" aria-label="Landhaus mit Holzbalkon und Terrasse" style="background:linear-gradient(#5a3a24 0%,#e8e6e0 40%,#b0a898 75%,#8a8070 100%)"></div>
      <div class="offer-caption"><span>Österreich, Tirol, Seefeld</span><svg class="doc-icon" viewBox="0 0 11 14"><path d="M1 1h6l3 3v9H1z" fill="#fff" stroke="#888"/></svg></div>
    </article>
  </section>

  <section class="more-bar">
    <svg class="more-arrow" viewBox="0 0 34 26"><path d="M2 2 L12 13 L2 24 H10 L20 13 L10 2Z" fill="#dfe8f6"/><path d="M14 2 L24 13 L14 24 H22 L32 13 L22 2Z" fill="#fff"/></svg>
    <div class="more-button">WEITERE <u>IMMOBILIENOBJEKTE</u>!</div>
  </section>

  <footer class="footer">
    <span>AGB</span>
    <span>Impressum/Kontakt</span>
    <span>Schnittstelle/Kooperationspartner</span>
    <div class="social">
      <span style="background:#3b5998"></span>
      <span style="background:#4aa8d8"></span>
      <span style="background:#d8d8d8"></span>
      <span style="background:#f08a24"></span>
      <span style="background:#333"></span>
      <span style="background:#3aa64a"></span>
    </div>
  </footer>

</body>
</html>
```